Company brochure

I would like to redesign our existing brochure.
It shall be trifold brochure with more modern and better appealing design than the old one. I am uploading the old one. The new design shall have all all information repeated from old brochure. It could be more or less pictures. I will provide more pictures if required. The keep text is important, the font shall be more modern. Brochure size shall be trifoldt US Legal size paper 8.5" x 14". I will provide all pitures, logos etc in a original format after design concept will be established or before on request.

Industry/Entity Type

It Company

Font styles to use
Other font styles liked:
• calibri

Colors
0555a3
3176b5
85abd2
0692cd
33a6d7
85cae6
1ab09a
33b8a4
87cfc6

Requirements
Nice to have
• I need all information from existing brochure such as text, customer logos, professional assos. logos to be shown in a new one. Picture could be added more.
Should not have
• No changes allowed to company letterhead. Only slight modifications allowed to company logo

```html
<!DOCTYPE html>
<html lang="en">
<head>
<meta charset="utf-8">
<title>Northpoint Refrigeration &amp; Air Conditioning – Trifold Brochure</title>
<link href="https://fonts.googleapis.com/css2?family=Open+Sans:wght@400;600;700&display=swap" rel="stylesheet">
<style>
:root{
  --navy:#0555a3;
  --blue:#3176b5;
  --sky:#33a6d7;
  --cyan:#0692cd;
  --pale:#85cae6;
  --paper:#eeeff1;
  --ink:#3a3a3a;
  --stage:#dcdcdc;
  --white:#ffffff;
}
*{box-sizing:border-box;margin:0;padding:0}
html,body{width:1001px;height:1200px;overflow:hidden}
body{background:var(--stage);font-family:"Open Sans",Arial,sans-serif;color:var(--ink);position:relative}
.sheet{position:absolute;left:75px;width:875px;height:531px;background:var(--paper);overflow:hidden;box-shadow:0 8px 10px -6px rgba(0,0,0,.35)}
.sheet-outside{top:39px}
.sheet-inside{top:623px}
.sheet-art{position:absolute;inset:0;width:875px;height:531px}
.abs{position:absolute}
.panel-heading{display:flex;align-items:center;gap:4px;font-weight:700;font-size:11px;text-transform:uppercase;line-height:1.4}
.panel-heading svg{flex:none}
.on-blue{color:var(--white)}
.on-blue .panel-heading{color:var(--white)}
.copy{font-size:8.6px;line-height:10.3px;text-align:justify;hyphens:auto}
.copy+.panel-heading{margin-top:9px}
.panel-heading+.copy{margin-top:4px}
.services{left:15px;top:143px;width:268px}
.quote-title{left:292px;width:293px;top:189px;text-align:center;color:var(--cyan);font-weight:700;font-size:10.5px;letter-spacing:.6px}
.pill{display:flex;align-items:center;justify-content:center;background:var(--navy);color:var(--white);font-weight:700;border-radius:14px;box-shadow:0 2px 3px rgba(0,0,0,.3)}
.contact-btn{left:375px;top:220px;width:127px;height:24px;font-size:11.5px}
.contact-lines{left:292px;width:293px;top:258px;text-align:center;font-size:10.5px;line-height:15.5px;color:#444}
.contact-lines .phone-row{display:flex;justify-content:center;align-items:center;gap:5px;margin-top:4px}
.badges{left:300px;width:277px;top:350px;display:flex;justify-content:space-around;align-items:center}
.badge{width:34px;height:34px;border-radius:50%;background:var(--blue);opacity:.85}
.badge.square{border-radius:3px;background:var(--navy)}
.tagline{left:292px;width:293px;top:457px;text-align:center;color:var(--white);font-weight:700;font-size:9.4px;letter-spacing:.5px}
.web{font-weight:700;font-size:14.5px;color:var(--sky);letter-spacing:.3px}
.web-b{right:300px;top:506px}
.web-c{right:9px;top:506px}
.brand{left:610px;top:22px;width:255px;display:flex;align-items:center;gap:10px}
.brand-mark{width:24px;height:24px;background:var(--white);flex:none}
.brand-name{color:var(--white);font-weight:700;font-size:12.5px;line-height:15px;text-align:center;text-transform:uppercase;letter-spacing:.4px}
.offer-list{left:602px;top:420px;list-style:none;color:var(--white);font-size:12px;line-height:16.6px}
.offer-list li{display:flex;align-items:center;gap:6px}
.offer-list li::before{content:"";width:7px;height:7px;border-radius:50%;background:var(--sky);flex:none}
.service{left:15px;top:30px;width:268px}
.service .panel-heading{color:var(--cyan)}
.emergency-btn{left:33px;top:55px;width:220px;height:29px;font-size:12.5px}
.service-copy{left:15px;top:98px;width:268px}
.service-copy .copy+.copy{margin-top:10px}
.middle{left:306px;top:140px;width:270px}
.middle .panel-heading{color:var(--cyan)}
.middle .copy+.panel-heading{margin-top:18px}
.projects{left:611px;top:209px;width:242px}
.projects .panel-heading{color:var(--cyan)}
.projects ul{list-style:none;font-size:8.7px;line-height:10.3px;margin-top:3px}
.projects li{margin-bottom:6px}
.clients-title{right:14px;top:483px;color:var(--white);font-weight:700;font-size:10.5px;letter-spacing:.3px}
.client-strip{left:0;top:505px;width:875px;height:26px;background:var(--white);display:flex;justify-content:space-around;align-items:center;padding:0 6px}
.client{font-weight:700;font-size:7.6px;color:var(--navy);white-space:nowrap}
</style>
</head>
<body>

<section class="sheet sheet-outside">
  <svg class="sheet-art" viewBox="0 0 875 531">
    <defs>
      <linearGradient id="navyFill" x1="0" y1="0" x2="1" y2="1">
        <stop offset="0" stop-color="#0a4f9c"/><stop offset="1" stop-color="#1f5fae"/>
      </linearGradient>
      <linearGradient id="plantTone" x1="0" y1="0" x2="1" y2="1">
        <stop offset="0" stop-color="#b9c6cf"/><stop offset=".5" stop-color="#7f9aa4"/><stop offset="1" stop-color="#4d7278"/>
      </linearGradient>
      <linearGradient id="roofTone" x1="0" y1="0" x2="0" y2="1">
        <stop offset="0" stop-color="#c9ced3"/><stop offset="1" stop-color="#8f979e"/>
      </linearGradient>
      <linearGradient id="motorTone" x1="0" y1="0" x2="1" y2="0">
        <stop offset="0" stop-color="#6b5a45"/><stop offset=".6" stop-color="#b99a5e"/><stop offset="1" stop-color="#d8c7a2"/>
      </linearGradient>
      <linearGradient id="paleGray" x1="0" y1="0" x2="0" y2="1">
        <stop offset="0" stop-color="#e9ebee"/><stop offset="1" stop-color="#d7dbe0"/>
      </linearGradient>
    </defs>
    <rect width="875" height="531" fill="url(#paleGray)"/>
    <rect x="0" y="100" width="292" height="340" fill="url(#navyFill)"/>
    <path role="img" aria-label="Photo of compressors and coloured piping in a machine room" d="M0 0H292V110C200 104 90 98 0 104Z" fill="url(#plantTone)"/>
    <path role="img" aria-label="Photo of insulated refrigeration pipe racks on a rooftop" d="M292 0H585V176C500 150 400 118 292 110Z" fill="url(#roofTone)"/>
    <path d="M585 0H875V116C790 122 680 150 585 180Z" fill="url(#navyFill)"/>
    <path role="img" aria-label="Photo of an engine room with white vessels and green compressors" d="M585 180C680 150 790 124 875 118V386C780 396 680 382 585 362Z" fill="url(#plantTone)"/>
    <path d="M585 362C680 382 780 396 875 386V531H585Z" fill="url(#navyFill)"/>
    <path d="M0 104C90 98 200 104 292 110C400 118 500 150 585 178" fill="none" stroke="#fff" stroke-width="4"/>
    <path d="M0 110C90 104 200 110 292 116C400 124 500 156 585 184" fill="none" stroke="var(--sky)" stroke-width="7"/>
    <path d="M585 180C680 150 790 124 875 118" fill="none" stroke="#fff" stroke-width="5"/>
    <path d="M585 362C680 382 780 396 875 386" fill="none" stroke="var(--sky)" stroke-width="6"/>
    <path role="img" aria-label="Photo of large motors in a compressor room" d="M0 420C120 412 220 414 292 418V531H0Z" fill="url(#motorTone)"/>
    <path d="M292 414C400 420 500 420 585 416V531H292Z" fill="url(#navyFill)"/>
    <path d="M0 402C120 396 220 400 292 406C400 414 500 412 585 404C700 396 800 378 875 360" fill="none" stroke="#fff" stroke-width="6"/>
    <path d="M0 410C120 404 220 408 292 414C400 422 500 420 585 412" fill="none" stroke="var(--sky)" stroke-width="8"/>
    <circle cx="806" cy="334" r="66" fill="#fff"/>
    <circle role="img" aria-label="Close-up photo of a compressor" cx="806" cy="334" r="59" fill="url(#roofTone)"/>
  </svg>

  <div class="abs services on-blue">
    <h2 class="panel-heading"><svg width="11" height="11" viewBox="0 0 12 12"><path d="M6 0V12M0 6H12M1.8 1.8L10.2 10.2M10.2 1.8L1.8 10.2" stroke="#85cae6" stroke-width="1.3"/></svg>Refrigeration Facilities Serviced</h2>
    <p class="copy">Food processing, cold storages and distribution facilities, meat and poultry processing plants, bakeries, dairies, beverage bottling facilities, ice production, chemical plants, refineries and ice rinks.</p>
    <h2 class="panel-heading"><svg width="11" height="11" viewBox="0 0 12 12"><path d="M6 0V12M0 6H12M1.8 1.8L10.2 10.2M10.2 1.8L1.8 10.2" stroke="#85cae6" stroke-width="1.3"/></svg>Industrial &amp; Commercial HVAC<br>Facilities Serviced</h2>
    <p class="copy">Production plant and manufacturing facilities, distribution and storage warehouses, office buildings, data centers, hospitals, colleges, shopping malls and country clubs.</p>
    <h2 class="panel-heading"><svg width="11" height="11" viewBox="0 0 12 12"><path d="M6 0V12M0 6H12M1.8 1.8L10.2 10.2M10.2 1.8L1.8 10.2" stroke="#85cae6" stroke-width="1.3"/></svg>Construction</h2>
    <p class="copy">Ammonia and freon refrigeration build-up systems. Refrigeration and HVAC equipment changeover. Freon packaged condensing units and chillers. Blast freezers, spiral and tunnel freezers. Computerized control, control and power wiring. Build-up glycol and water chillers. Air handlers and evaporators. Refrigeration, glycol, chill water and process piping. Certified X-ray quality welding. Carbon steel, stainless steel, copper, PVC and sanitary piping. Hot tapping available.</p>
  </div>

  <p class="abs quote-title">GET A FREE QUOTE &amp; SURVEY</p>
  <div class="abs pill contact-btn">CONTACT US</div>
  <div class="abs contact-lines">
    <p>4150 Harrow Lane</p>
    <p>Westbrook, CA 90412</p>
    <p class="phone-row">
      <svg width="12" height="10" viewBox="0 0 12 10"><path d="M1 3C1 1 3 1 6 1S11 1 11 3L9 4 8 3H4L3 4ZM3 5H9L10 9H2Z" fill="var(--cyan)"/></svg>555-201-0142
      <svg width="11" height="11" viewBox="0 0 11 11"><rect x="2" y="0" width="6" height="4" fill="none" stroke="var(--cyan)"/><rect x="0" y="4" width="11" height="7" rx="1" fill="var(--cyan)"/></svg>555-201-0178
    </p>
    <p>info@northpointrac.com</p>
  </div>
  <div class="abs badges" aria-label="Professional association memberships">
    <span class="badge square"></span><span class="badge"></span><span class="badge square"></span><span class="badge"></span>
  </div>
  <p class="abs tagline">CUSTOMER SATISFACTION IS OUR ULTIMATE GOAL</p>
  <p class="abs web web-b">www.northpointrac.com</p>

  <div class="abs brand">
    <span class="brand-mark"></span>
    <p class="brand-name">Northpoint Refrigeration<br>&amp;<br>Air Conditioning</p>
  </div>
  <ul class="abs offer-list">
    <li>Industrial ♦ Commercial</li>
    <li>Ammonia ♦ Freon ♦ CO2</li>
    <li>Design ♦ Engineering</li>
    <li>Service ♦ Maintenance</li>
    <li>Construction</li>
  </ul>
  <p class="abs web web-c">www.northpointrac.com</p>
</section>

<section class="sheet sheet-inside">
  <svg class="sheet-art" viewBox="0 0 875 531">
    <defs>
      <linearGradient id="paperFade" x1="0" y1="0" x2="1" y2="0">
        <stop offset="0" stop-color="#f3f4f6"/><stop offset=".66" stop-color="#eceef1"/><stop offset="1" stop-color="#e6ecf3"/>
      </linearGradient>
      <linearGradient id="weldTone" x1="0" y1="0" x2="1" y2="0">
        <stop offset="0" stop-color="#2a5c9c"/><stop offset=".45" stop-color="#8aa2c2"/><stop offset=".7" stop-color="#d8c9c0"/><stop offset="1" stop-color="#6c7f9e"/>
      </linearGradient>
      <linearGradient id="skyTone" x1="0" y1="0" x2="0" y2="1">
        <stop offset="0" stop-color="#eef3f8" stop-opacity="0"/><stop offset="1" stop-color="#b9cbe0"/>
      </linearGradient>
      <linearGradient id="roomTone" x1="0" y1="0" x2="0" y2="1">
        <stop offset="0" stop-color="#eef0f2" stop-opacity="0"/><stop offset=".35" stop-color="#9fb4ba"/><stop offset="1" stop-color="#5b7f86"/>
      </linearGradient>
      <linearGradient id="navyFill2" x1="0" y1="0" x2="1" y2="0">
        <stop offset="0" stop-color="#0a4f9c"/><stop offset="1" stop-color="#1f5fae"/>
      </linearGradient>
    </defs>
    <rect width="875" height="531" fill="url(#paperFade)"/>
    <path role="img" aria-label="Photo of a welder at work with sparks" d="M300 0H875V150C790 162 700 160 590 130C500 108 420 60 330 20Z" fill="url(#weldTone)"/>
    <path d="M330 20C420 60 500 108 590 130C700 160 790 162 875 150V172C790 184 700 182 590 152C500 130 420 84 330 40Z" fill="url(#navyFill2)"/>
    <rect role="img" aria-label="Photo of a city skyline with a helicopter lifting equipment" x="585" y="185" width="290" height="230" fill="url(#skyTone)"/>
    <rect role="img" aria-label="Photo of a compressor room with green equipment and red valves" x="0" y="370" width="660" height="100" fill="url(#roomTone)"/>
    <path d="M0 452C250 425 600 440 875 390V505H0Z" fill="#fff"/>
    <path d="M0 458C250 431 600 446 875 396V505H0Z" fill="var(--sky)"/>
    <path d="M0 468C250 441 600 456 875 406V505H0Z" fill="url(#navyFill2)"/>
    <circle cx="352" cy="63" r="52" fill="#85cae6"/>
    <circle role="img" aria-label="Photo of an evaporative condenser unit" cx="352" cy="63" r="45" fill="#aab8c2"/>
  </svg>

  <div class="abs service">
    <h2 class="panel-heading"><svg width="11" height="11" viewBox="0 0 12 12"><path d="M6 0V12M0 6H12M1.8 1.8L10.2 10.2M10.2 1.8L1.8 10.2" stroke="#33a6d7" stroke-width="1.3"/></svg>Service and Maintenance</h2>
  </div>
  <div class="abs pill emergency-btn">24 hour Emergency Service</div>
  <div class="abs service-copy">
    <p class="copy">Ammonia and Freon. Customized maintenance program. Troubleshooting service and repair of refrigeration and HVAC systems including all mechanical, structural, electrical and control components. Compressor rebuilding as well as vibration and oil analysis. Refrigerant conversion and recovery.</p>
    <p class="copy">Build-up ammonia and freon refrigeration systems, packaged freon refrigeration units, blast freezing/cooling systems, spiral and tunnel freezers, holding freezers and coolers, evaporators, glycol and water chillers, ice production machines, process rooms.</p>
    <p class="copy">Compressors, evaporative and air-cool condensers, recirculation packages, ammonia, water and glycol pumps, heat exchangers, control valves and regulators, electrical motors. Safety devices test, repair and calibration including: relief valves, leak detectors, pressure and temperature sensors, level switches and interlock devices.</p>
    <p class="copy">Packaged and split gas/electric air conditioners, heat pumps. Air handlers, exhaust fans, swamp coolers, water chillers, water towers and pumps. Exhaust and ventilation, humidification and dehumidification, clean rooms. Boilers and Boiler Piping. Refrigeration and Building Control and automation. PLC, VFD, VSD, VAV.</p>
  </div>

  <div class="abs middle">
    <h2 class="panel-heading"><svg width="11" height="11" viewBox="0 0 12 12"><path d="M6 0V12M0 6H12M1.8 1.8L10.2 10.2M10.2 1.8L1.8 10.2" stroke="#33a6d7" stroke-width="1.3"/></svg>Experience</h2>
    <p class="copy">Thirty plus years in industrial, commercial, ammonia and freon refrigeration and air conditioning. Experienced in all aspects of refrigeration projects, from design concept through execution, with the ability to cost-effectively satisfy customer requirements within aggressive time frames.</p>
    <h2 class="panel-heading"><svg width="11" height="11" viewBox="0 0 12 12"><path d="M6 0V12M0 6H12M1.8 1.8L10.2 10.2M10.2 1.8L1.8 10.2" stroke="#33a6d7" stroke-width="1.3"/></svg>Engineering Services</h2>
    <p class="copy">Design ammonia and freon systems. Build-up and packaged refrigeration systems. Liquid recirculating, flooded, and DX systems. Low and high temperature chillers. Glycol and chill water distribution systems.<br>Energy saving and expansion projects. 3D SolidForm and DraftCAD drawings. Computerized control design and implementation, PLC, VFD. Mechanical integrity surveys, safety and hazard analysis, seismic assessment. Safety programs, PSM, RMP, CalARP, MOC, SOP. Regulatory Compliance and Professional training.</p>
  </div>

  <div class="abs projects">
    <h2 class="panel-heading"><svg width="11" height="11" viewBox="0 0 12 12"><path d="M6 0V12M0 6H12M1.8 1.8L10.2 10.2M10.2 1.8L1.8 10.2" stroke="#33a6d7" stroke-width="1.3"/></svg>Major Projects Completed</h2>
    <ul>
      <li>• 675 TR, 1960 HP ammonia refrigeration system for a bakery.</li>
      <li>• 90 TR, 400 HP freon spiral blast freezer for meat processing plant.</li>
      <li>• 920 TR, 1420 HP ammonia refrigeration system for meat processing facility.</li>
      <li>• 1300 TR freon chiller and glycol chiller and glycol distribution system for a dairy processing plant.</li>
      <li>• An ammonia refrigeration system for 560,000 sq. ft cold storage and food distribution facility.</li>
      <li>• 480 ton ice production facility.</li>
      <li>• 375 TR, 1500 HP ice-cream plant.</li>
    </ul>
  </div>

  <p class="abs clients-title">COMPANIES WE PROUDLY SERVE</p>
  <div class="abs client-strip">
    <span class="client">Valebrook</span><span class="client">Crestmart</span><span class="client">Outfield</span><span class="client">Hillcrest Medical</span><span class="client">Fizzwell</span><span class="client">Morrow</span><span class="client">Redgate</span><span class="client">Orbis</span><span class="client">Harbor Aero</span><span class="client">Bakehouse</span><span class="client">Northfield</span><span class="client">Oventa</span><span class="client">Grainly</span><span class="client">Calderwood</span><span class="client">Sabrosa</span><span class="client">Nordale</span><span class="client">Coldline</span><span class="client">Juno</span>
  </div>
</section>

</body>
</html>
```